Real Estate Business Cards

Looking for a clean, sharp and professional look for our Real Estate investment Fund that invests in Multi Family Apartment buildings.

Target Market(s)

Real Estate Fund

Industry/Entity Type

Real Estate

Contact Information for Business Card

Company Description: Real Estate Investment Fund
Company Name: RKW Holdings
Name: Marcus Olvane
Cell: (917) 482-0657
Email: marcus@rkwholdings-example.com
Website: www.rkwholdings-example.com
Address: 418, 9th Street, Brooklyn NY 11218

Colors

Designer to choose colors to be used in the design.

Requirements
Nice to have
• Colors to match logo

```html
<!DOCTYPE html>
<html lang="en">
<head>
<meta charset="utf-8">
<title>RKW Holdings – Business Card</title>
<link rel="stylesheet" href="https://fonts.googleapis.com/css2?family=Lato:wght@400;900&display=swap">
<style>
  :root {
    --stage: #2b2b2d;
    --paper: #f4f4f2;
    --brand-blue: #1769a8;
    --back-blue: #1a72ad;
    --ink: #3d3d40;
    --rule: #a9c3d9;
    --back-text: #d6dde3;
  }
  * { margin: 0; padding: 0; box-sizing: border-box; }
  html, body { width: 1200px; height: 946px; overflow: hidden; }
  body {
    background: var(--stage);
    font-family: "Lato", Arial, sans-serif;
    position: relative;
  }
  .card {
    position: absolute;
    left: 290px;
    width: 620px;
    height: 354px;
    box-shadow: 0 18px 40px rgba(0,0,0,.45);
  }
  .card--front { top: 89px; background: var(--paper); }
  .card--back  { top: 503px; background: var(--back-blue); }

  .wordmark {
    position: absolute;
    display: flex;
    align-items: center;
    gap: 14px;
    font-weight: 400;
    text-transform: uppercase;
    letter-spacing: .12em;
  }
  .card--front .wordmark { left: 130px; top: 62px; font-size: 30px; color: var(--brand-blue); }
  .wordmark__mark { width: 44px; height: 44px; background: var(--brand-blue); flex: none; }

  .card--back .wordmark {
    left: 0; right: 0; top: 150px; justify-content: center;
    font-size: 42px; color: var(--back-text);
  }
  .card--back .wordmark__mark { width: 58px; height: 58px; background: rgba(255,255,255,.18); }

  .identity {
    position: absolute;
    right: 340px;
    top: 222px;
    text-align: right;
  }
  .identity__name {
    font-weight: 900;
    font-size: 24px;
    color: var(--brand-blue);
    letter-spacing: .01em;
    white-space: nowrap;
  }
  .identity__title { font-size: 14px; color: var(--ink); margin-top: 2px; }

  .divider {
    position: absolute;
    left: 300px;
    top: 180px;
    width: 1px;
    height: 130px;
    background: var(--rule);
  }

  .contact {
    position: absolute;
    left: 322px;
    top: 178px;
    font-size: 13.5px;
    color: var(--ink);
    line-height: 1.3;
  }
  .contact__company { color: var(--brand-blue); }
  .contact__list { list-style: none; margin-top: 4px; }
  .contact__list li { display: flex; align-items: center; gap: 8px; height: 19px; }
  .contact__list svg { width: 13px; height: 13px; fill: var(--brand-blue); flex: none; }
</style>
</head>
<body>
  <section class="card card--front">
    <div class="wordmark"><span class="wordmark__mark"></span>RKW Holdings</div>

    <div class="identity">
      <div class="identity__name">MARCUS OLVANE</div>
      <div class="identity__title">Founder &amp; CEO</div>
    </div>

    <div class="divider"></div>

    <div class="contact">
      <div class="contact__company">RKW Holdings</div>
      <div>418, 9th Street,</div>
      <div>Brooklyn NY 11218</div>
      <ul class="contact__list">
        <li>
          <svg viewBox="0 0 24 24" aria-hidden="true"><path d="M6.6 10.8a15.1 15.1 0 0 0 6.6 6.6l2.2-2.2c.3-.3.7-.4 1-.2 1.1.4 2.3.6 3.6.6.6 0 1 .4 1 1V20c0 .6-.4 1-1 1A17 17 0 0 1 3 4c0-.6.4-1 1-1h3.5c.6 0 1 .4 1 1 0 1.3.2 2.5.6 3.6.1.3 0 .7-.2 1z"/></svg>
          (917) 482-0657
        </li>
        <li>
          <svg viewBox="0 0 24 24" aria-hidden="true"><path d="M2 5h20v14H2z M2 5l10 8 10-8" fill="none" stroke="#1769a8" stroke-width="2"/></svg>
          marcus@rkwholdings-example.com
        </li>
        <li>
          <svg viewBox="0 0 24 24" aria-hidden="true"><circle cx="12" cy="12" r="10" fill="none" stroke="#1769a8" stroke-width="2"/><path d="M2 12h20M12 2c3 3 3 17 0 20M12 2c-3 3-3 17 0 20" fill="none" stroke="#1769a8" stroke-width="1.6"/></svg>
          www.rkwholdings-example.com
        </li>
      </ul>
    </div>
  </section>

  <section class="card card--back">
    <div class="wordmark"><span class="wordmark__mark"></span>RKW Holdings</div>
  </section>
</body>
</html>
```